Website for Youth Orchestra to sell tickets and attract young musicians

We are looking for a new website design for a Youth Orchestra; one of the best classical youth orchestras in the county. This project is the design only. <br/><br/>The website serves two main purposes:<br/>• Selling tickets for concerts and performances of the orchestra<br/>• Recruiting young musicians to do audition for the orchestra<br/>
Updates

Need extra days to review

Target Market(s)

Classical music lovers with a special interest in young upcoming musicians.
Young talented musicians

Number of Pages Required

2 page

Colors
ec1f27

Requirements
Must have
• - A Picture on the front page that promotes the main upcomming event
• - Attention for recruiting new musicians
• - Pictures with young musicians (white back ground, see examples)
• - Responsive
• - Please use the logo attached
Should not have
• The brown colors of the current website (kvb-velmorin.example)

```html
<!DOCTYPE html>
<html lang="en">
<head>
<meta charset="utf-8">
<title>Footer – Velmorin Youth Orchestra</title>
<link rel="stylesheet" href="https://fonts.googleapis.com/css2?family=Poppins:wght@400;500;600;700&family=Lora:ital@1&display=swap">
<style>
:root{
  --brand-red:#ea3640;
  --pill-red:#ef5a62;
  --ink:#2b2b33;
  --muted:#cfcfd3;
  --line-grey:#e6e6e8;
  --paper:#ffffff;
  --dot-tint:#fbfbfc;
  --wave-tint:#f6f6f7;
}
*{margin:0;padding:0;box-sizing:border-box}
html,body{width:1054px;height:1200px;overflow:hidden;background:var(--paper)}
.board{position:relative;width:1054px;height:1200px;font-family:"Poppins",sans-serif;color:var(--ink)}
.dot-field{position:absolute;left:15px;top:15px;width:615px;height:605px;background:var(--dot-tint)}
.dot-block{position:absolute;left:32px;top:1050px;width:141px;height:150px;background:#f8f8f9}
.wave-field{position:absolute;left:790px;top:918px;width:246px;height:132px;background:linear-gradient(180deg,#fff 0%,var(--wave-tint) 50%,#fff 100%)}
.backdrop-ring{position:absolute;left:79px;top:243px;width:778px;height:778px;border:1px solid var(--line-grey);border-radius:50%}
.section-title{position:absolute;left:61px;top:32px;font-weight:700;font-size:32px;color:var(--brand-red);letter-spacing:-.5px}
.section-intro{position:absolute;left:90px;top:100px;width:385px;font-family:"Lora",serif;font-style:italic;font-size:15px;line-height:23.6px;color:var(--ink)}
.section-count{position:absolute;left:797px;top:1120px;font-weight:700;font-size:32px;color:var(--muted);letter-spacing:-.3px}

.footer-card{position:absolute;left:176px;top:331px;width:700px;height:534px;border-radius:23px;overflow:hidden;background:var(--paper);box-shadow:0 14px 40px rgba(0,0,0,.16)}
.insta-strip{position:relative;height:224px}
.insta-tile{position:absolute;top:33px;width:145px;height:145px}
.insta-tile .glyph{position:absolute;right:7px;top:7px;width:9px;height:9px;border:1.2px solid rgba(255,255,255,.85);border-radius:2.5px}
.tile-poster{left:51px;background:linear-gradient(135deg,#e6d3ea 0%,#e9cbe0 45%,#f06a3c 70%,#dccbe6 100%)}
.tile-player{left:247px;background:linear-gradient(160deg,#1a1612 0%,#4a3426 50%,#120e0b 100%)}
.tile-portrait{left:443px;background:linear-gradient(160deg,#eceae6 0%,#d9cfc4 50%,#8a5a34 80%,#e9e6e2 100%)}
.tile-soloist{left:638px;background:linear-gradient(120deg,#e4d2bd 0%,#c9a88a 60%,#2a2522 100%)}

.site-footer{position:absolute;left:0;top:224px;width:700px;height:310px;background:var(--brand-red);color:#fff}
.footer-nav{position:absolute;left:51px;top:18px;display:grid;grid-template-columns:100px 101px 150px;row-gap:12px}
.footer-nav a{color:#fff;text-decoration:none;font-size:8.6px;font-weight:500;line-height:15px}
.newsletter{position:absolute;left:471px;top:21px;width:215px}
.newsletter .accent{width:35px;height:2.5px;background:#fff}
.newsletter h2{margin-top:13px;font-size:11px;font-weight:700;white-space:nowrap}
.newsletter p{margin-top:11px;font-size:7px;font-weight:500}
.subscribe{margin-top:17px;width:203px;height:24px;border-radius:12px;background:var(--pill-red);display:flex;align-items:center;justify-content:space-between;padding:0 11px 0 18px;font-size:8.3px;font-weight:500}
.footer-rule{position:absolute;left:24px;top:150px;width:651px;height:1px;background:rgba(255,255,255,.18)}
.social{position:absolute;left:0;right:0;top:187px;display:flex;justify-content:center;gap:28px}
.social span{width:8px;height:8px;background:#fff;border-radius:2px}
.copyright{position:absolute;left:0;right:0;top:220px;text-align:center;font-size:7px;font-weight:500;letter-spacing:.1px}
.footer-name{position:absolute;left:0;right:0;top:246px;text-align:center;font-size:12px;font-weight:500;line-height:13px}
</style>
</head>
<body>
<div class="board">
  <div class="dot-field" role="img" aria-label="Faint dot grid background pattern"></div>
  <div class="dot-block" role="img" aria-label="Dense dot pattern decoration"></div>
  <div class="wave-field" role="img" aria-label="Decorative wavy line pattern"></div>
  <div class="backdrop-ring"></div>

  <h1 class="section-title">Footer</h1>
  <p class="section-intro">As the user reach the end of the site's navigation. We would like to offer them a useful links that the user can also access in the menu. This is also the best way to offer a registration for news letter in able to keep in touch through mail. We also want to offer social media links. An instagram post slider to provide latest insights.</p>

  <div class="footer-card">
    <div class="insta-strip">
      <div class="insta-tile tile-poster" role="img" aria-label="Instagram post: New Year concert poster"><span class="glyph"></span></div>
      <div class="insta-tile tile-player" role="img" aria-label="Instagram post: young violinist playing on a dark stage"><span class="glyph"></span></div>
      <div class="insta-tile tile-portrait" role="img" aria-label="Instagram post: violinist portrait on a white background"><span class="glyph"></span></div>
      <div class="insta-tile tile-soloist" role="img" aria-label="Instagram post: musician with bow, partly visible"></div>
    </div>

    <footer class="site-footer">
      <nav class="footer-nav">
        <a href="#">Home</a><a href="#">Orchestra</a><a href="#">Play Along</a>
        <a href="#">Concerts</a><a href="#">Tours</a><a href="#">Partners</a>
        <a href="#">Friends</a><a href="#">Former Members</a><a href="#">Contact &amp; Organization</a>
      </nav>

      <div class="newsletter">
        <div class="accent"></div>
        <h2>New to Velmorin Youth Orchestra?</h2>
        <p>Sign up to our newsletter to get the latest news.</p>
        <div class="subscribe">
          <span>Subscribe to our Newsletter</span>
          <svg width="13" height="11" viewBox="0 0 13 11"><path d="M1 1 L12 5.5 L1 10 L3 5.5 Z" fill="none" stroke="#fff" stroke-width="1.1" stroke-linejoin="round"/></svg>
        </div>
      </div>

      <div class="footer-rule"></div>
      <div class="social">
        <span role="img" aria-label="Social network link 1"></span>
        <span role="img" aria-label="Social network link 2"></span>
        <span role="img" aria-label="Social network link 3"></span>
        <span role="img" aria-label="Social network link 4"></span>
        <span role="img" aria-label="Video channel link"></span>
      </div>
      <p class="copyright">COPYRIGHT 2020 VELMORINS JEUGD ORKEST. UX/UI BY LENA BRANDT</p>
      <p class="footer-name">velmorins<br>jeugd orkest</p>
    </footer>
  </div>

  <p class="section-count">section 06/06</p>
</div>
</body>
</html>
```